Willowmere Commons Shopping Center Brochure

Take the three attached files, request any additional information that may be needed and produce an attractive and effective pdf marketing brochure that will help make our shopping center lease up.  Would prefer most, if not all, of the text in the word file to be included.  Other than that parameter we are looking for a winning look.  The attached pdf file has too much information and ONLY page one should be used.  We would like all the tables and accompanying text in the Excel workbook to be used.
Thank you!

Target Market(s)
Entrepreneurs who need a commercial retail space to operate their businesses from.
Industry/Entity Type
Marketing

```html
<!DOCTYPE html>
<html lang="en">
<head>
<meta charset="UTF-8">
<title>Willowmere Commons Shopping Center – Back Cover</title>
<link rel="stylesheet" href="https://fonts.googleapis.com/css2?family=Arimo:wght@400;700&display=swap">
<style>
  :root {
    --blue-center: #2f4e9c;
    --blue-mid: #29427f;
    --blue-edge: #213565;
    --text-light: #ffffff;
  }
  html, body {
    margin: 0;
    padding: 0;
    width: 800px;
    height: 1200px;
    overflow: hidden;
    background: var(--blue-edge);
  }
  .back-cover {
    position: relative;
    width: 800px;
    height: 1200px;
    background: radial-gradient(ellipse 620px 760px at 414px 600px,
      var(--blue-center) 0%,
      var(--blue-mid) 50%,
      var(--blue-edge) 100%);
    font-family: "Arimo", Arial, sans-serif;
    color: var(--text-light);
  }
  .contact-block {
    position: absolute;
    left: 0;
    right: 0;
    top: 1011px;
    text-align: center;
    font-size: 17px;
    line-height: 22.6px;
    text-shadow: 0 1px 2px rgba(0, 0, 0, 0.45);
  }
  .contact-block p {
    margin: 0;
  }
  .contact-company {
    font-weight: 700;
  }
</style>
</head>
<body>
  <main class="back-cover">
    <address class="contact-block" style="font-style: normal;">
      <p class="contact-company">Fernbrook Holdings, LLC dba Willowmere Commons</p>
      <p class="contact-mail">P.O. Box 2418</p>
      <p class="contact-city">Maplecrest, TX 75519</p>
      <p class="contact-phone">555-214-7390</p>
      <p class="contact-web">www.willowmerecommons.com</p>
      <p class="contact-email">info@willowmerecommons.com</p>
    </address>
  </main>
</body>
</html>
```